Fabric Softener

We need fabric softener. Bottle picture attached for reference. Color of bottle can be proposed as well. Normally bottle is pink and blue color

Logo is also attached that shall be used.
Updates

Need extra days to review

Low designer entries

Target Market(s)

Niche

Font styles to use
Sans Serif

Requirements
Must have
• Fabric, Brightness, Nature
Nice to have
• Good colors
Should not have
• Adults

```html
<!DOCTYPE html>
<html lang="en">
<head>
<meta charset="utf-8">
<title>Lumora Fabric Softener – Label</title>
<link rel="stylesheet" href="https://fonts.googleapis.com/css2?family=Lobster&display=swap">
<style>
  :root {
    --backdrop: #3f3b6e;
    --label-deep: #3c3f92;
    --label-mid: #5257aa;
    --label-light: #9aa1dc;
    --label-edge: #ffffff;
    --name-panel: #6a58a6;
    --type-white: #ffffff;
    --type-outline: #5b4a9e;
  }
  html, body {
    margin: 0;
    padding: 0;
    overflow: hidden;
  }
  body {
    width: 942px;
    height: 1200px;
    background: var(--backdrop);
    position: relative;
  }
  .product-label {
    position: absolute;
    left: 84px;
    top: 89px;
    width: 773px;
    height: 1022px;
    overflow: visible;
  }
  .label-edge {
    fill: none;
    stroke: var(--label-edge);
    stroke-width: 5;
  }
  .name-panel {
    fill: var(--name-panel);
  }
  .script {
    font-family: "Lobster", cursive;
    fill: var(--type-white);
    text-anchor: middle;
  }
  .script--outlined {
    stroke: var(--type-outline);
    stroke-width: 7;
    paint-order: stroke fill;
    stroke-linejoin: round;
  }
  .tagline { font-size: 56px; }
  .brand-name { font-size: 100px; }
  .product-type { font-size: 84px; }
</style>
</head>
<body>
  <svg class="product-label" viewBox="0 0 644 852" xmlns="http://www.w3.org/2000/svg">
    <defs>
      <linearGradient id="label-floral-tone" x1="0.1" y1="0.2" x2="0.95" y2="0.85">
        <stop offset="0" stop-color="var(--label-deep)"/>
        <stop offset="0.45" stop-color="var(--label-mid)"/>
        <stop offset="0.7" stop-color="#7d84cc"/>
        <stop offset="1" stop-color="var(--label-light)"/>
      </linearGradient>
    </defs>

    <path class="label-artwork"
          role="img"
          aria-label="Floral pattern of white flowers, curling vines, leaves and butterflies on deep blue to soft lavender tones"
          fill="url(#label-floral-tone)"
          d="M187,7 C120,60 10,250 2,462 C-5,700 90,830 260,845 C420,858 600,780 640,650 C660,560 600,510 520,495 C420,475 330,440 290,300 C260,190 250,60 222,32 C210,15 197,4 187,7 Z"/>
    <path class="label-edge"
          d="M187,7 C120,60 10,250 2,462 C-5,700 90,830 260,845 C420,858 600,780 640,650 C660,560 600,510 520,495 C420,475 330,440 290,300 C260,190 250,60 222,32 C210,15 197,4 187,7 Z"/>

    <text class="script script--outlined tagline" x="207" y="444">Fabric Protect</text>

    <rect class="name-panel" x="114" y="482" width="346" height="156"/>
    <text class="script brand-name" x="287" y="600">Lumora</text>

    <text class="script script--outlined product-type" x="348" y="714">Fabric Softener</text>
  </svg>
</body>
</html>
```